Meadowlark in a league of it's own

Meadowlark is a pan European contact center.
We serve our clients in 18 languages from Antwerp in Belgium, Fez in Morocco and with our partner Vellorix.
We have a presentation and we would like to make it much more visible;
Less text, more images or animation.
Our business case is based on three elements with three colours :
blue sky : because we ar fully organized in the cloud,
Green : in our customer care college, out green village we put a lot of energy in training,
Orange : when technology is good and people have a good knowledge, passion will come...
Eventually we are ready to payfor some stock images - to negotiate-
For answers to your questions : tom.ravelin@brinkmail.be

```html
<!DOCTYPE html>
<html lang="en">
<head>
<meta charset="utf-8">
<title>Meadowlark – Presentation Slides</title>
<link href="https://fonts.googleapis.com/css2?family=Open+Sans:ital,wght@0,300;0,400;0,600;1,400&display=swap" rel="stylesheet">
<style>
  :root {
    --orange: #e4572e;
    --green: #8cb63c;
    --blue: #0e96d2;
    --backdrop: #5b5c5e;
    --ink: #555;
    --muted: #8a8a8a;
    --rule: #cfcfcf;
    --band: #8c8c8c;
  }
  * { box-sizing: border-box; margin: 0; padding: 0; }
  html, body { width: 1200px; height: 900px; overflow: hidden; }
  body { background: var(--backdrop); font-family: "Open Sans", Arial, sans-serif; color: var(--ink); position: relative; }
  .slide { position: absolute; width: 357px; height: 276px; background: #fff; overflow: hidden; }
  .s1 { left: 47px; top: 186px; } .s2 { left: 418px; top: 186px; } .s3 { left: 785px; top: 186px; }
  .s4 { left: 47px; top: 471px; } .s5 { left: 418px; top: 471px; } .s6 { left: 785px; top: 471px; }
  .abs { position: absolute; }
  .slide-title { position: absolute; left: 24px; top: 18px; font-weight: 300; font-size: 16px; color: var(--blue); letter-spacing: -0.3px; }
  .brand { position: absolute; display: flex; align-items: center; gap: 3px; font-weight: 600; color: #333; }
  .brand i { display: block; border-radius: 50%; background: var(--orange); }
  .footer .brand { left: 10px; top: 253px; font-size: 7px; }
  .footer .brand i { width: 7px; height: 7px; }
  .footer .rule { position: absolute; left: 52px; right: 26px; top: 258px; border-top: 1px solid var(--rule); }
  .footer .page { position: absolute; left: 334px; top: 254px; width: 8px; height: 8px; border-radius: 50%; background: var(--blue); color: #fff; font-size: 4px; text-align: center; line-height: 8px; }
  .photo { position: absolute; background: linear-gradient(135deg, #d9d9d9, #a9a9a9 60%, #cfcfcf); }
  .tiny { font-size: 4px; line-height: 5.2px; color: var(--muted); }
  /* welcome */
  .welcome .brand { left: 18px; top: 36px; font-size: 15px; font-weight: 400; }
  .welcome .brand i { width: 14px; height: 14px; }
  .welcome h1 { position: absolute; left: 18px; top: 134px; font-weight: 300; font-size: 14px; color: var(--blue); }
  .welcome h2 { position: absolute; left: 18px; top: 151px; font-weight: 400; font-size: 9px; letter-spacing: 1.5px; color: #444; border-bottom: 1px solid #444; padding-right: 4px; }
  .welcome .date { position: absolute; left: 18px; top: 166px; font-size: 5px; color: var(--muted); }
  .welcome .legal { position: absolute; left: 19px; top: 253px; width: 240px; }
  /* agenda */
  .agenda-item { position: absolute; left: 94px; display: flex; align-items: center; }
  .num { width: 27px; height: 27px; border-radius: 50%; color: #fff; font-weight: 300; font-size: 13px; display: flex; align-items: center; justify-content: center; }
  .agenda-item .tick { width: 9px; height: 1px; background: currentColor; position: relative; margin-left: 1px; }
  .agenda-item .tick::after { content: ""; position: absolute; right: -2px; top: -1.5px; width: 4px; height: 4px; border-radius: 50%; background: currentColor; }
  .agenda-item .bar { width: 1px; height: 26px; background: var(--rule); margin: 0 8px 0 2px; }
  .agenda-item h3 { font-weight: 400; font-size: 7px; color: var(--blue); }
  .agenda-item p { width: 120px; margin-top: 1px; }
  .orange { background: var(--orange); color: var(--orange); } .green { background: var(--green); color: var(--green); } .blue { background: var(--blue); color: var(--blue); }
  .num.orange, .num.green, .num.blue { color: #fff; }
  .agenda-item.c-orange { color: var(--orange); } .agenda-item.c-green { color: var(--green); } .agenda-item.c-blue { color: var(--blue); }
  /* about */
  .about-lead { position: absolute; left: 23px; top: 136px; width: 108px; font-size: 5px; line-height: 9.5px; color: var(--blue); text-transform: uppercase; }
  .about-body { position: absolute; left: 142px; top: 133px; width: 192px; font-size: 5px; line-height: 9.3px; text-align: justify; color: #666; }
  .about-body p + p { margin-top: 9px; }
  .band { position: absolute; left: 0; right: 0; top: 61px; height: 66px; background: var(--band); }
  .band-text { position: absolute; left: 161px; top: 75px; width: 176px; font-style: italic; font-size: 6px; line-height: 12.6px; color: #fff; text-align: justify; }
  .about-body2 { position: absolute; left: 161px; top: 146px; width: 176px; font-size: 6px; line-height: 12.6px; color: #666; text-align: justify; }
  /* flow */
  .flow-col { position: absolute; top: 137px; width: 70px; text-align: left; }
</style>
</head>
<body>

<section class="slide s1 welcome">
  <svg class="abs" width="357" height="276" viewBox="0 0 357 276">
    <path d="M113 0 C 150 90, 220 200, 357 212" fill="none" stroke="#777" stroke-width="0.6"/>
    <line x1="149" y1="165" x2="161" y2="182" stroke="#888" stroke-width="0.6"/>
    <line x1="161" y1="182" x2="178" y2="205" stroke="#888" stroke-width="0.6"/>
    <line x1="178" y1="205" x2="159" y2="219" stroke="#888" stroke-width="0.6"/>
    <line x1="178" y1="205" x2="205" y2="195" stroke="#888" stroke-width="0.6"/>
    <line x1="290" y1="140" x2="335" y2="126" stroke="#888" stroke-width="0.6"/>
    <circle cx="149" cy="165" r="3" fill="var(--orange)"/>
    <circle cx="161" cy="182" r="4" fill="var(--green)"/>
    <circle cx="178" cy="205" r="9" fill="var(--orange)"/>
    <circle cx="159" cy="219" r="4" fill="var(--blue)"/>
    <circle cx="335" cy="126" r="9" fill="var(--green)"/>
    <circle cx="250" cy="164" r="55" fill="#fff" stroke="var(--blue)" stroke-width="6"/>
  </svg>
  <div class="photo" style="left:198px;top:112px;width:104px;height:104px;border-radius:50%;" role="img" aria-label="Smiling call centre agent wearing a headset"></div>
  <div class="brand"><i></i>Meadowlark</div>
  <h1>WELCOME</h1>
  <h2>To Our Presentation</h2>
  <div class="date">August 2014</div>
  <p class="legal tiny">Contains Confidential and Proprietary information and may not be disclosed, redistributed or reproduced in whole or in part without prior written consent of Meadowlark, Inc.</p>
</section>

<section class="slide s2">
  <h2 class="slide-title">AGENDA</h2>
  <div class="agenda-item c-orange" style="top:63px"><div class="num orange">1</div><span class="tick"></span><span class="bar"></span><div><h3>LOREM IPSUM DOLOR SIT MET</h3><p class="tiny">Lorem ipsum dolor sit amet, conse ctetur adipiscing elit, sed do eiusmod tempor incididunt ut labore</p></div></div>
  <div class="agenda-item c-green" style="top:96px"><div class="num green">2</div><span class="tick"></span><span class="bar"></span><div><h3>LOREM IPSUM DOLOR SIT MET</h3><p class="tiny">Lorem ipsum dolor sit amet, conse ctetur adipiscing elit, sed do eiusmod tempor incididunt ut labore</p></div></div>
  <div class="agenda-item c-blue" style="top:129px"><div class="num blue">3</div><span class="tick"></span><span class="bar"></span><div><h3>LOREM IPSUM DOLOR SIT MET</h3><p class="tiny">Lorem ipsum dolor sit amet, conse ctetur adipiscing elit, sed do eiusmod tempor incididunt ut labore</p></div></div>
  <div class="agenda-item c-green" style="top:163px"><div class="num green">4</div><span class="tick"></span><span class="bar"></span><div><h3>LOREM IPSUM DOLOR SIT MET</h3><p class="tiny">Lorem ipsum dolor sit amet, conse ctetur adipiscing elit, sed do eiusmod tempor incididunt ut labore</p></div></div>
  <div class="agenda-item c-orange" style="top:196px"><div class="num orange">5</div><span class="tick"></span><span class="bar"></span><div><h3>LOREM IPSUM DOLOR SIT MET</h3><p class="tiny">Lorem ipsum dolor sit amet, conse ctetur adipiscing elit, sed do eiusmod tempor incididunt ut labore</p></div></div>
  <footer class="footer"><div class="brand"><i></i>Meadowlark</div><span class="rule"></span><span class="page">2</span></footer>
</section>

<section class="slide s3">
  <h2 class="slide-title">ABOUT US</h2>
  <div class="photo" style="left:23px;top:46px;width:311px;height:74px;" role="img" aria-label="Row of call centre agents with headsets at their desks"></div>
  <p class="about-lead">Lorem ipsum dolor sit met consectur adipscing elit, sed do euismod tempor incidiunt ut labore et delore magna</p>
  <div class="about-body">
    <p>Lorem ipsum dolor sit amet, consectetur adipisicing elit, sed do eiusmod tempor incididunt ut labore et dolore magna aliqua. Ut enim ad minim veniam, quis nostrud exercitation ullamco laboris nisi ut aliquip ex ea commodo consequat. Duis aute irure dolor in reprehenderit in voluptate velit esse cillum dolore eu fugiat nulla pariatur.</p>
    <p>Lorem ipsum dolor sit amet, consectetur adipisicing elit, sed do eiusmod tempor incididunt ut labore et dolore magna aliqua. Ut enim ad minim veniam, quis nostrud exercitation ullamco laboris nisi ut aliquip ex ea commodo consequat. Duis aute irure dolor in reprehenderit in voluptate velit esse cillum dolore eu</p>
  </div>
  <footer class="footer"><div class="brand"><i></i>Meadowlark</div><span class="rule"></span><span class="page">2</span></footer>
</section>

<section class="slide s4">
  <h2 class="slide-title">ABOUT US</h2>
  <div class="band"></div>
  <div class="photo" style="left:14px;top:48px;width:131px;height:87px;" role="img" aria-label="Team lead with headset standing in front of agents in an office"></div>
  <p class="band-text"><b style="font-weight:400">Lorem ipsum dolor sit amet</b><br>consectetur adipisicing elit, sed do eiusmod tempor incididunt ut labore et dolore magna aliqua. Ut enim ad minim veniam, quis nostrud exercitation ullamco laboris</p>
  <p class="about-body2">Lorem ipsum dolor sit amet, consectetur adipisicing elit, sed do eiusmod tempor incididunt ut labore et dolore magna aliqua. Ut enim ad minim veniam, quis nostrud exercitation ullamco laboris nisi ut aliquip ex ea commodo consequat. Duis aute irure dolor in reprehenderit in voluptate velit esse cillum dolore eu fugiat nulla pariatur. Lorem ipsum dolor sit amet, consectetur adipisicing elit, sed do eiusmod tempor incididunt ut labore et dolore</p>
  <footer class="footer"><div class="brand"><i></i>Meadowlark</div><span class="rule"></span><span class="page">2</span></footer>
</section>

<section class="slide s5">
  <h2 class="slide-title">OUT OF THE COLUMNS</h2>
  <svg class="abs" width="357" height="276" viewBox="0 0 357 276">
    <path d="M18 127 C 70 118, 140 122, 200 140 S 300 170, 337 208" fill="none" stroke="#666" stroke-width="0.7"/>
    <circle cx="18" cy="127" r="2" fill="#444"/><circle cx="337" cy="208" r="2" fill="#444"/>
    <g stroke-width="0.7">
      <line x1="69" y1="123" x2="69" y2="110" stroke="var(--green)"/><circle cx="69" cy="110" r="1.8" fill="var(--green)"/>
      <line x1="123" y1="126" x2="123" y2="139" stroke="var(--orange)"/><circle cx="123" cy="139" r="1.8" fill="var(--orange)"/>
      <line x1="178" y1="134" x2="178" y2="121" stroke="var(--blue)"/><circle cx="178" cy="121" r="1.8" fill="var(--blue)"/>
      <line x1="232" y1="147" x2="232" y2="160" stroke="var(--green)"/><circle cx="232" cy="160" r="1.8" fill="var(--green)"/>
      <line x1="286" y1="171" x2="286" y2="158" stroke="var(--orange)"/><circle cx="286" cy="158" r="1.8" fill="var(--orange)"/>
    </g>
    <g font-family="Open Sans, sans-serif" font-size="5" fill="#fff" text-anchor="middle">
      <circle cx="69" cy="123" r="6" fill="var(--green)"/><text x="69" y="125">1</text>
      <circle cx="123" cy="126" r="6" fill="var(--orange)"/><text x="123" y="128">2</text>
      <circle cx="178" cy="134" r="6" fill="var(--blue)"/><text x="178" y="136">3</text>
      <circle cx="232" cy="147" r="6" fill="var(--green)"/><text x="232" y="149">4</text>
      <circle cx="286" cy="171" r="6" fill="var(--orange)"/><text x="286" y="173">5</text>
    </g>
  </svg>
  <p class="abs tiny" style="left:47px;top:77px;width:48px;color:#555">Lorem ipsum dolor sit amet, consectetur adipisicing elit, sed do eiusmod tempor incididunt ut labore et dolore magna aliqua.</p>
  <p class="abs tiny" style="left:102px;top:144px;width:48px;color:#555">Lorem ipsum dolor sit amet, consectetur adipisicing elit, sed do eiusmod tempor incididunt ut labore et dolore magna aliqua.</p>
  <p class="abs tiny" style="left:156px;top:88px;width:48px;color:#555">Lorem ipsum dolor sit amet, consectetur adipisicing elit, sed do eiusmod tempor incididunt ut labore et dolore magna aliqua.</p>
  <p class="abs tiny" style="left:210px;top:166px;width:48px;color:#555">Lorem ipsum dolor sit amet, consectetur adipisicing elit, sed do eiusmod tempor incididunt ut labore et dolore magna aliqua.</p>
  <p class="abs tiny" style="left:265px;top:126px;width:48px;color:#555">Lorem ipsum dolor sit amet, consectetur adipisicing elit, sed do eiusmod tempor incididunt ut labore et dolore magna aliqua.</p>
  <footer class="footer"><div class="brand"><i></i>Meadowlark</div><span class="rule"></span><span class="page">2</span></footer>
</section>

<section class="slide s6">
  <h2 class="slide-title">OUR FLOW</h2>
  <svg class="abs" width="357" height="276" viewBox="0 0 357 276">
    <line x1="25" y1="128" x2="326" y2="128" stroke="var(--rule)" stroke-width="0.7"/>
    <g stroke-width="0.7">
      <line x1="61" y1="115" x2="61" y2="128" stroke="var(--orange)"/><circle cx="61" cy="128" r="1.8" fill="var(--orange)"/>
      <line x1="138" y1="115" x2="138" y2="128" stroke="var(--green)"/><circle cx="138" cy="128" r="1.8" fill="var(--green)"/>
      <line x1="214" y1="115" x2="214" y2="128" stroke="var(--blue)"/><circle cx="214" cy="128" r="1.8" fill="var(--blue)"/>
      <line x1="291" y1="115" x2="291" y2="128" stroke="var(--orange)"/><circle cx="291" cy="128" r="1.8" fill="var(--orange)"/>
    </g>
    <g stroke-width="1.2" fill="none">
      <path d="M92 99 h11 M100 96 l3 3 l-3 3" stroke="var(--orange)"/>
      <path d="M169 99 h11 M177 96 l3 3 l-3 3" stroke="var(--green)"/>
      <path d="M245 99 h11 M253 96 l3 3 l-3 3" stroke="var(--blue)"/>
    </g>
    <g font-family="Open Sans, sans-serif" font-size="13" font-weight="300" fill="#fff" text-anchor="middle">
      <circle cx="61" cy="99" r="16" fill="var(--orange)"/><text x="61" y="104">1</text>
      <circle cx="138" cy="99" r="16" fill="var(--green)"/><text x="138" y="104">2</text>
      <circle cx="214" cy="99" r="16" fill="var(--blue)"/><text x="214" y="104">3</text>
      <circle cx="291" cy="99" r="16" fill="var(--orange)"/><text x="291" y="104">4</text>
    </g>
  </svg>
  <p class="flow-col tiny" style="left:26px;color:#555">Lorem ipsum dolor sit amet, consectetur adipiscing elit, sed do eiusmod tempor incididunt ut labore et dolore magna aliqua. Ut enim ad minim veniam, quis nostrud exercitation ullamco laboris nisi ut aliquip ex ea commodo consequat. Duis aute irure dolor in reprehenderit in voluptate velit esse cillum dolore eu fugiat nulla pariatur. Excepteur sint occaecat cupidatat non proident, sunt in culpa qui officia deserunt mollit anim id est laborum.</p>
  <p class="flow-col tiny" style="left:103px;color:#555">Lorem ipsum dolor sit amet, consectetur adipiscing elit, sed do eiusmod tempor incididunt ut labore et dolore magna aliqua. Ut enim ad minim veniam, quis nostrud exercitation ullamco laboris nisi ut aliquip ex ea commodo consequat. Duis aute irure dolor in reprehenderit in voluptate velit esse cillum dolore eu fugiat nulla pariatur. Excepteur sint occaecat cupidatat non proident, sunt in culpa qui officia deserunt mollit anim id est laborum.</p>
  <p class="flow-col tiny" style="left:180px;color:#555">Lorem ipsum dolor sit amet, consectetur adipiscing elit, sed do eiusmod tempor incididunt ut labore et dolore magna aliqua. Ut enim ad minim veniam, quis nostrud exercitation ullamco laboris nisi ut aliquip ex ea commodo consequat. Duis aute irure dolor in reprehenderit in voluptate velit esse cillum dolore eu fugiat nulla pariatur. Excepteur sint occaecat cupidatat non proident, sunt in culpa qui officia deserunt mollit anim id est laborum.</p>
  <p class="flow-col tiny" style="left:257px;color:#555">Lorem ipsum dolor sit amet, consectetur adipiscing elit, sed do eiusmod tempor incididunt ut labore et dolore magna aliqua. Ut enim ad minim veniam, quis nostrud exercitation ullamco laboris nisi ut aliquip ex ea commodo consequat. Duis aute irure dolor in reprehenderit in voluptate velit esse cillum dolore eu fugiat nulla pariatur. Excepteur sint occaecat cupidatat non proident, sunt in culpa qui officia deserunt mollit anim id est laborum.</p>
  <footer class="footer"><div class="brand"><i></i>Meadowlark</div><span class="rule"></span><span class="page">2</span></footer>
</section>

</body>
</html>
```